Manufacturing company needs new business card.

I need a unique Business Card that will truly stand out. Nothing too busy. Simple is good, right? Not looking for a standard design either. No cookie cutter layout. I am just looking for something interesting and a bit different. Does't have to completely off the wall crazy, just not your run of the mill business card. Clean and modern with a touch of industrial.

Target Market(s)

Air conditioning industry, Architects, builders.

Industry/Entity Type

Business

Contact Information for Business Card

Details to be included on card are:

Peter Walsh
Managing Director

T: 1300 418 592
M: 0427 385 914
W: www.brandvalefabrication.com.au
E: peter.walsh@brandvalefabrication.com.au
A: 58 Harlow Lane, Sydney NSW 2000

Font styles to use
Sans Serif

Colors
0355a3
848484
fbfbfb

Requirements
Must have
• Card design must be landscape.

```html
<!DOCTYPE html>
<html lang="en">
<head>
<meta charset="utf-8">
<title>Brandvale Fabrication – Business Card</title>
<link href="https://fonts.googleapis.com/css2?family=Lato:wght@400;700&display=swap" rel="stylesheet">
<style>
  :root {
    --navy: #1f2f6e;
    --brand-blue: #0355a3;
    --grey: #848484;
    --ink: #3a3a3a;
    --card: #f1f2f3;
    --stage: #d8d3cb;
    --white: #fbfbfb;
  }
  * { margin: 0; padding: 0; box-sizing: border-box; }
  html, body { width: 1200px; height: 970px; overflow: hidden; }
  body {
    background: var(--stage);
    font-family: "Lato", Arial, sans-serif;
    position: relative;
  }
  .business-card {
    position: absolute;
    left: 50px;
    top: 172px;
    width: 1100px;
    height: 626px;
    background: var(--card);
    border: 1px solid #c9cacc;
    box-shadow: 0 10px 30px rgba(0,0,0,0.12);
    overflow: hidden;
  }
  .brand-square {
    position: absolute;
    left: 0;
    top: 120px;
    width: 300px;
    height: 300px;
    background: var(--navy);
    opacity: 0.92;
  }
  .company {
    position: absolute;
    left: 402px;
    top: 104px;
    width: 660px;
  }
  .company-name {
    font-weight: 700;
    font-size: 61px;
    line-height: 1;
    color: var(--navy);
    letter-spacing: -0.5px;
    white-space: nowrap;
  }
  .company-region {
    display: flex;
    align-items: center;
    gap: 18px;
    margin-top: 14px;
  }
  .company-rule {
    flex: 0 0 226px;
    height: 3px;
    background: var(--ink);
  }
  .company-region-text {
    font-weight: 700;
    font-size: 34px;
    line-height: 1;
    letter-spacing: 19px;
    color: var(--navy);
    white-space: nowrap;
  }
  .person {
    position: absolute;
    left: 402px;
    top: 286px;
    display: flex;
    align-items: center;
    white-space: nowrap;
  }
  .person-name {
    font-weight: 700;
    font-size: 37px;
    color: var(--navy);
    letter-spacing: -0.5px;
  }
  .person-divider {
    width: 2px;
    height: 36px;
    background: var(--ink);
    margin: 0 14px 0 16px;
  }
  .person-title {
    font-size: 30px;
    color: var(--ink);
  }
  .contact-list {
    position: absolute;
    left: 402px;
    top: 364px;
    list-style: none;
  }
  .contact-item {
    display: flex;
    align-items: center;
    height: 38px;
    font-size: 29px;
    color: var(--ink);
    white-space: nowrap;
  }
  .contact-icon {
    width: 30px;
    height: 30px;
    margin-right: 10px;
    flex: 0 0 30px;
  }
</style>
</head>
<body>
  <section class="business-card">
    <div class="brand-square" role="img" aria-label="Brand mark area"></div>

    <header class="company">
      <div class="company-name">Brandvale Fabrication</div>
      <div class="company-region">
        <span class="company-rule"></span>
        <span class="company-region-text">AUSTRALIA</span>
      </div>
    </header>

    <div class="person">
      <span class="person-name">PETER WALSH</span>
      <span class="person-divider"></span>
      <span class="person-title">Managing Director</span>
    </div>

    <ul class="contact-list">
      <li class="contact-item">
        <svg class="contact-icon" viewBox="0 0 30 30" aria-hidden="true">
          <rect width="30" height="30" fill="var(--navy)"/>
          <path d="M7 12c0-3 4-4 8-4s8 1 8 4l-3 1-1-2h-8l-1 2z M10 14h10l2 8H8z" fill="var(--white)"/>
          <circle cx="15" cy="18" r="2.5" fill="var(--navy)"/>
        </svg>
        <span>1300 418 592</span>
      </li>
      <li class="contact-item">
        <svg class="contact-icon" viewBox="0 0 30 30" aria-hidden="true">
          <rect width="30" height="30" fill="var(--navy)"/>
          <rect x="10" y="5" width="10" height="20" rx="1.5" fill="none" stroke="var(--white)" stroke-width="1.8"/>
          <rect x="12" y="8" width="6" height="7" fill="var(--white)"/>
          <path d="M12 18h6M12 21h6" stroke="var(--white)" stroke-width="1.5"/>
        </svg>
        <span>0427 385 914</span>
      </li>
      <li class="contact-item">
        <svg class="contact-icon" viewBox="0 0 30 30" aria-hidden="true">
          <rect width="30" height="30" fill="var(--navy)"/>
          <rect x="5" y="8" width="20" height="14" fill="none" stroke="var(--white)" stroke-width="1.8"/>
          <path d="M5 8l10 8 10-8M5 22l7-7M25 22l-7-7" fill="none" stroke="var(--white)" stroke-width="1.5"/>
        </svg>
        <span>peter.walsh@brandvalefabrication.com.au</span>
      </li>
      <li class="contact-item">
        <svg class="contact-icon" viewBox="0 0 30 30" aria-hidden="true">
          <rect width="30" height="30" fill="var(--navy)"/>
          <circle cx="15" cy="15" r="9" fill="none" stroke="var(--white)" stroke-width="1.6"/>
          <ellipse cx="15" cy="15" rx="4" ry="9" fill="none" stroke="var(--white)" stroke-width="1.3"/>
          <path d="M6 15h18M8 10h14M8 20h14" stroke="var(--white)" stroke-width="1.2"/>
        </svg>
        <span>www.brandvalefabrication.com.au</span>
      </li>
      <li class="contact-item">
        <svg class="contact-icon" viewBox="0 0 30 30" aria-hidden="true">
          <rect width="30" height="30" fill="var(--navy)"/>
          <path d="M15 25c-4-5-7-9-7-12a7 7 0 0 1 14 0c0 3-3 7-7 12z" fill="none" stroke="var(--white)" stroke-width="1.8"/>
          <circle cx="15" cy="13" r="2.5" fill="var(--white)"/>
        </svg>
        <span>58 Harlow Lane, Sydney NSW 2000</span>
      </li>
    </ul>
  </section>
</body>
</html>
```